redesign my website coralhopvoyages.net and make it user friendly

I already have a website, coralhopvoyages.net, and want a redesign in WordPress with Elementor Pro, using the same text/content. The goal is to improve:

Design quality (colors, fonts, spacing, visual flow)
User experience (easy navigation, clear offers)
Conversion readiness (calls-to-action, trust signals, booking flow)
Technical side (SEO basics, fast speed, full mobile responsiveness)

The site should look modern, clean, fun, engaging, interactive and optimized for speed and usability.

I would like the 11 page to be consolidate dto 6 as follows: Home (main landing, highlights)

Sailboat Trips (all packages, itineraries, pricing)
Boats (fleet details, features, photos)
How It Works (booking process, FAQs, travel info, what to expect)
Blog
Contact Us (form, WhatsApp, phone, etc.)

Target Market(s)

sailboat trip customers for San Blas Islands in Panama

Industry/Entity Type

Travel, Boat Tour Agency

Coding

Coded - Design and coding required

Number of Pages Required

3 page

Font styles to use
Sans Serif
Other font styles liked:
• Oswalg and sans serif

Colors
0054AA
0677BA
7BADD7
CADEEF
E8F1F8
0094D4
00A9DD
6FCCEA
C7EBF8
E9F6FB
FFC000
F8CF3A
FAE287
FDF2CF
FEFAEE
F0912C
F2A743
F7CA91
FBE8D2
FDF5EE

Requirements
Must have
• Home (main landing, highlights) Sailboat Trips (all packages, itineraries, pricing) Boats (fleet details, features, photos) How It Works (booking process, FAQs, travel info, what to expect) Blog (updates, travel tips, inspiration) Contact Us (form, WhatsApp, phone, etc.)
Nice to have
• I want it to look professionla and be very user friendy to entice people to contact me to book boat trips
Should not have
• a store

```html
<!DOCTYPE html>
<html lang="en">
<head>
<meta charset="utf-8">
<title>Coral Hop Voyages – Website Layouts</title>
<link rel="stylesheet" href="https://fonts.googleapis.com/css2?family=Oswald:wght@500;600&family=Josefin+Sans:wght@300;400&family=Poppins:wght@400;500;600&display=swap">
<style>
:root{
  --board:#a9a9a9;
  --white:#ffffff;
  --ink:#2b3a44;
  --muted:#5d6a72;
  --teal:#17607a;
  --teal-dark:#0c3a4a;
  --orange:#f0912c;
  --orange-soft:#f2a743;
  --blue-btn:#2d4fe0;
  --sea-1:#0f5f86;
  --sea-2:#2a8fb5;
  --sea-3:#7bc3dc;
  --line:#e3e8ec;
  --sky:#e9f6fb;
  --head:'Josefin Sans',sans-serif;
  --display:'Oswald',sans-serif;
  --body:'Poppins',sans-serif;
}
*{box-sizing:border-box;margin:0;padding:0}
html,body{width:1200px;height:3033px;overflow:hidden;background:var(--board);font-family:var(--body);color:var(--ink)}
.screen{position:absolute;background:var(--white);overflow:hidden}
.abs{position:absolute}
.desktop{left:111px;top:69px;width:520px;height:2893px}
.mobile-a{left:672px;top:69px;width:184px;height:1789px}
.mobile-b{left:898px;top:69px;width:184px;height:1244px}

.logo{font-family:var(--display);font-weight:600;color:var(--teal-dark);letter-spacing:.2px}
.btn{display:flex;align-items:center;justify-content:center;gap:4px;border-radius:20px;color:var(--white);font-weight:500;white-space:nowrap}
.btn-orange{background:var(--orange)}
.btn-navy{background:var(--teal-dark)}
.btn-blue{background:var(--blue-btn)}
.nav a{position:absolute;font-size:6.5px;color:var(--ink);text-decoration:none;font-weight:500;letter-spacing:.2px}

.photo-sea{background:linear-gradient(180deg,#5aa9c6 0%,#2a86ad 40%,#0f5f86 70%,#0b4a6a 100%)}
.photo-lagoon{background:linear-gradient(160deg,#7fc6d4 0%,#3fa3b8 45%,#1f7d9c 100%)}
.photo-deck{background:linear-gradient(160deg,#c9d6de 0%,#8aa3b3 50%,#4e7287 100%)}
.photo-party{background:linear-gradient(160deg,#9cc4d6 0%,#d8c7b4 50%,#6b8fa3 100%)}
.photo-sunset{background:linear-gradient(180deg,#b9c4cc 0%,#e2b6a0 30%,#6c8ea1 55%,#2d5f79 100%)}
.photo-bay{background:linear-gradient(180deg,#bfe3ee 0%,#74c0d6 55%,#3d93b1 100%)}

.hero-title{font-family:var(--display);font-weight:500;color:var(--white);line-height:1}
.sec-title{font-family:var(--head);font-weight:300;color:var(--teal);text-align:center;line-height:1.2;text-transform:uppercase}
.sec-title::after{content:"";display:block;width:5px;height:5px;border-radius:50%;background:var(--orange);margin:6px auto 0}

.card{background:var(--white);border-radius:10px;box-shadow:0 2px 8px rgba(20,50,70,.16);overflow:visible}
.card-photo{border-radius:10px;overflow:hidden}
.pkg-type{font-size:7px;font-weight:600;color:var(--ink)}
.pkg-name{font-size:12px;font-weight:500;color:var(--teal)}
.pkg-meta{display:flex;gap:7px;font-size:6px;color:var(--muted);align-items:center}
.pkg-meta i{display:inline-block;width:6px;height:6px;background:var(--orange-soft);border-radius:2px;margin-right:2px;vertical-align:-1px}
.pkg-note{font-size:5.6px;color:var(--ink)}

.tour-title{font-weight:500;color:var(--orange);text-align:center;line-height:1.15}
.tour-text{color:var(--muted);text-align:center;line-height:1.55}
.icon-bubble{position:absolute;border-radius:50%;background:var(--orange);display:flex;align-items:center;justify-content:center;border:2px solid var(--white)}

.arrow{position:absolute;border-radius:50%;display:flex;align-items:center;justify-content:center;font-size:8px}
.arrow-light{background:var(--white);box-shadow:0 1px 4px rgba(0,0,0,.18);color:var(--muted)}
.arrow-orange{background:var(--orange);color:var(--white)}
.sq-arrow{position:absolute;display:flex;align-items:center;justify-content:center;font-size:9px}

.dots{position:absolute;display:flex;gap:3px;justify-content:center}
.dots span{width:4px;height:4px;border-radius:50%;border:1px solid var(--orange)}
.dots span.on{background:var(--orange)}

.feature{position:absolute;background:var(--white);border-radius:4px;box-shadow:0 2px 6px rgba(20,50,70,.15);display:flex;align-items:center}
.feature .fic{border-radius:50%;background:var(--orange);flex:none;display:flex;align-items:center;justify-content:center}
.feature h4{font-weight:500;color:var(--teal)}
.feature p{color:var(--muted);line-height:1.45}

.review{position:absolute;border:1px solid var(--line);border-radius:10px;background:var(--white)}
.review p{font-style:italic;color:var(--muted);line-height:1.6}
.quote{position:absolute;font-family:var(--display);color:var(--orange);font-weight:600;line-height:1}
.rating{position:absolute;display:flex;align-items:center;gap:2px}
.rating b{display:block;border-radius:50%;background:#c9d3da}
.rating span{color:var(--orange-soft);letter-spacing:-.5px}
.person{position:absolute;display:flex;align-items:center;gap:5px}
.avatar{border-radius:50%;background:linear-gradient(160deg,#c2ccd2,#5f7482)}
.person strong{display:block;font-weight:600;color:var(--ink)}
.person small{display:block;color:var(--muted)}

.form-bg{background:linear-gradient(180deg,#ffffff 0%,#e6f3f7 35%,#a6d3e0 70%,#4f9cb8 100%)}
.form-panel{position:absolute;border-radius:12px;background:rgba(198,230,238,.55)}
.field{position:absolute;background:var(--white);border:1px solid #dbe4ea;color:var(--muted);display:flex;align-items:center;justify-content:space-between}

.footer{background:var(--teal-dark);color:var(--white)}
.foot-head{position:absolute;font-weight:500;color:#8fd0e6;letter-spacing:.2px}
.foot-list{position:absolute;list-style:none;color:#e6eef2}
.foot-list li::before{content:"» ";color:#8fb8c7}
.contact-row{position:absolute;display:flex;gap:6px;align-items:flex-start;color:#e6eef2;line-height:1.3}
.contact-row i{flex:none;border:1px solid #cfe2ea;border-radius:2px;display:flex;align-items:center;justify-content:center}
.news-input{position:absolute;background:#1c6f8e;color:#dfeff5;display:flex;align-items:center;font-weight:500}
.news-btn{position:absolute;background:var(--orange);color:var(--white);display:flex;align-items:center;justify-content:center;font-weight:500}
.socials{position:absolute;display:flex;gap:4px}
.socials span{border:1px solid #cfe2ea;border-radius:2px;display:block}
</style>
</head>
<body>

<!-- ================= DESKTOP HOME ================= -->
<section class="screen desktop">
  <header class="abs" style="left:0;top:0;width:520px;height:60px;background:#f3f9fc">
    <div class="abs logo" style="left:28px;top:27px;font-size:13px">Coral Hop Voyages</div>
    <div class="abs btn btn-orange" style="left:361px;top:12px;width:61px;height:17px;font-size:6px">BOOK NOW</div>
    <div class="abs btn btn-navy" style="left:429px;top:12px;width:62px;height:17px;font-size:6px">CONTACT US</div>
    <nav class="nav">
      <a style="left:234px;top:39px">SAIL BOAT TRIPS</a>
      <a style="left:320px;top:39px">OUR BOAT</a>
      <a style="left:385px;top:39px">PLAN YOUR TRIP</a>
      <a style="left:469px;top:39px">BLOG</a>
    </nav>
  </header>

  <div class="abs photo-sea" role="img" aria-label="Catamaran and sailboat anchored on open turquoise sea under a blue sky" style="left:0;top:60px;width:520px;height:357px"></div>
  <div class="arrow arrow-light" style="left:4px;top:218px;width:16px;height:16px;opacity:.4">‹</div>
  <div class="arrow arrow-light" style="left:492px;top:218px;width:18px;height:18px;color:var(--ink)">›</div>
  <h1 class="abs hero-title" style="left:46px;top:152px;font-size:44px">San Blas Islands</h1>
  <p class="abs" style="left:51px;top:202px;font-size:8.5px;color:var(--white)">Panama Sailing Vacations,Ultimate Beaches &amp; Catamaran Tours</p>
  <div class="abs btn btn-orange" style="left:48px;top:233px;width:128px;height:25px;font-size:8px">CHARTER INQUIRY FORM <span>↦</span></div>
  <div class="dots" style="left:240px;top:376px"><span class="on" style="background:#fff;border-color:#fff"></span><span style="border-color:#fff"></span><span style="border-color:#fff"></span><span style="border-color:#fff"></span></div>

  <h2 class="abs sec-title" style="left:110px;top:442px;width:300px;font-size:21px">Featured Sailing<br>Tour Packages</h2>
  <div class="sq-arrow" style="left:449px;top:465px;width:20px;height:24px;background:#fff;box-shadow:0 1px 4px rgba(0,0,0,.18);color:var(--muted)">‹</div>
  <div class="sq-arrow" style="left:471px;top:465px;width:20px;height:24px;background:var(--orange);color:#fff">›</div>

  <article class="abs card" style="left:29px;top:522px;width:145px;height:231px">
    <div class="abs card-photo photo-lagoon" role="img" aria-label="Aerial view of a white catamaran over clear shallow water" style="left:5px;top:5px;width:135px;height:122px"></div>
    <div class="abs" style="left:12px;top:138px;width:125px">
      <div class="pkg-type">Catamaran</div>
      <div class="pkg-name">Aurora 42</div>
      <div class="pkg-meta" style="margin-top:4px"><span><i></i>42 ft</span><span><i></i>3 cabin</span><span><i></i>8 Guest</span></div>
      <div class="pkg-note" style="margin-top:6px">Service that exceeds all expectations!</div>
    </div>
    <div class="abs btn btn-blue" style="left:45px;top:222px;width:56px;height:11px;font-size:5.5px">INFO &amp; PRICE</div>
  </article>
  <article class="abs card" style="left:187px;top:522px;width:145px;height:231px">
    <div class="abs card-photo photo-bay" role="img" aria-label="Catamaran moored beside a palm covered island" style="left:5px;top:5px;width:135px;height:122px"></div>
    <div class="abs" style="left:12px;top:138px;width:125px">
      <div class="pkg-type">Catamaran</div>
      <div class="pkg-name">Tidewind 55F</div>
      <div class="pkg-meta" style="margin-top:4px"><span><i></i>55 ft</span><span><i></i>4 cabin</span><span><i></i>8 Guest</span></div>
      <div class="pkg-note" style="margin-top:6px">Luxury and elegance on water!</div>
    </div>
    <div class="abs btn btn-blue" style="left:45px;top:222px;width:56px;height:11px;font-size:5.5px">INFO &amp; PRICE</div>
  </article>
  <article class="abs card" style="left:345px;top:522px;width:146px;height:231px">
    <div class="abs card-photo photo-deck" role="img" aria-label="Deck of a catamaran with red cushions and water toys" style="left:5px;top:5px;width:136px;height:122px"></div>
    <div class="abs" style="left:12px;top:138px;width:125px">
      <div class="pkg-type">Catamaran</div>
      <div class="pkg-name">Tidewind 55S</div>
      <div class="pkg-meta" style="margin-top:4px"><span><i></i>20 ft</span><span><i></i>4 cabin</span><span><i></i>9 Guest</span></div>
      <div class="pkg-note" style="margin-top:6px">Safest family fun at sea!</div>
    </div>
    <div class="abs btn btn-blue" style="left:45px;top:222px;width:56px;height:11px;font-size:5.5px">INFO &amp; PRICE</div>
  </article>

  <div class="abs btn btn-orange" style="left:179px;top:797px;width:161px;height:27px;font-size:9px">SEE ALL BOATS &amp; PRICES <span>↦</span></div>

  <h2 class="abs sec-title" style="left:90px;top:870px;width:340px;font-size:21px">Discover Ultimate<br>Panama Sailing Tours</h2>

  <article class="abs card" style="left:29px;top:969px;width:146px;height:230px">
    <div class="abs card-photo photo-party" role="img" aria-label="Couple walking along a marina dock" style="left:8px;top:10px;width:130px;height:100px"></div>
    <div class="icon-bubble" style="left:55px;top:-14px;width:36px;height:36px"><svg width="16" height="16" viewBox="0 0 24 24" fill="none" stroke="#fff" stroke-width="2"><circle cx="12" cy="5" r="2"/><path d="M12 7v14M6 11h12M4 14a8 7 0 0 0 16 0"/></svg></div>
    <h3 class="abs tour-title" style="left:0;top:121px;width:146px;font-size:10.5px">Private Charters</h3>
    <p class="abs tour-text" style="left:12px;top:138px;width:122px;font-size:6px">Sail the beautiful islands and beaches of San Blas on a private all-inclusive catamaran. Enjoy a custom itinerary, friendly crew, and flexible options to fit any budget—perfect for a relaxing escape.</p>
  </article>
  <article class="abs card" style="left:187px;top:969px;width:146px;height:230px">
    <div class="abs card-photo photo-party" role="img" aria-label="Group of friends celebrating on a sailboat deck" style="left:8px;top:10px;width:130px;height:100px"></div>
    <div class="icon-bubble" style="left:55px;top:-14px;width:36px;height:36px"><svg width="16" height="16" viewBox="0 0 24 24" fill="none" stroke="#fff" stroke-width="2"><circle cx="8" cy="6" r="2.5"/><circle cx="16" cy="6" r="2.5"/><path d="M4 21v-8a4 4 0 0 1 8 0v8M12 21v-8a4 4 0 0 1 8 0v8"/></svg></div>
    <h3 class="abs tour-title" style="left:0;top:121px;width:146px;font-size:10.5px">Shared Charters</h3>
    <p class="abs tour-text" style="left:12px;top:138px;width:122px;font-size:6px">Share the experience with others for a more affordable alternative to a private charter. Perfect for couples, solo travelers, and small groups—enjoy San Blas beaches, clear waters, great meals, and a relaxed atmosphere with a welcoming crew.</p>
  </article>
  <article class="abs card" style="left:345px;top:969px;width:146px;height:230px">
    <div class="abs card-photo photo-bay" role="img" aria-label="Sailboat on calm turquoise water" style="left:8px;top:10px;width:130px;height:100px"></div>
    <div class="icon-bubble" style="left:55px;top:-14px;width:36px;height:36px"><svg width="16" height="16" viewBox="0 0 24 24" fill="none" stroke="#fff" stroke-width="2"><path d="M3 15h18l-3 5H6zM6 15V9h12v6M10 9V5h4v4"/></svg></div>
    <h3 class="abs tour-title" style="left:0;top:121px;width:146px;font-size:10.5px">Family Friendly<br>Boat Trips</h3>
    <p class="abs tour-text" style="left:12px;top:150px;width:122px;font-size:6px">San Blas is perfect for kids, with calm waters, safe snorkeling, and fun island-hopping. Families love the mix of adventure and culture—an ideal way to explore Panama</p>
  </article>

  <h2 class="abs sec-title" style="left:40px;top:1280px;width:440px;font-size:21px">Island Adventures &amp; Activities</h2>
  <div class="abs card-photo photo-deck" role="img" aria-label="Friends cheering on the bow of a sailing yacht" style="left:78px;top:1345px;width:365px;height:194px;border-radius:12px"></div>
  <div class="abs" style="left:78px;top:1470px;width:365px;height:69px;border-radius:0 0 12px 12px;background:linear-gradient(180deg,rgba(15,95,134,0) 0%,rgba(15,95,134,.85) 100%)"></div>
  <div class="abs" style="left:78px;top:1480px;width:365px;text-align:center;font-family:var(--display);font-size:16px;color:#fff;font-weight:500">SAILING</div>
  <p class="abs" style="left:110px;top:1504px;width:300px;text-align:center;font-size:7px;line-height:1.5;color:#fff">Set sail across sparkling waters, hopping from one island group to another, each offering new beaches, and breathtaking views</p>
  <div class="arrow arrow-light" style="left:36px;top:1434px;width:18px;height:18px">‹</div>
  <div class="arrow arrow-orange" style="left:463px;top:1434px;width:18px;height:18px">›</div>
  <div class="dots" style="left:240px;top:1564px"><span class="on"></span><span></span><span></span><span></span><span></span><span></span><span></span></div>

  <h2 class="abs sec-title" style="left:110px;top:1630px;width:300px;font-size:21px">Why Book With Us</h2>
  <div class="feature" style="left:31px;top:1697px;width:220px;height:62px;padding:0 8px;gap:10px">
    <div class="fic" style="width:40px;height:40px"><svg width="18" height="18" viewBox="0 0 24 24" fill="none" stroke="#fff" stroke-width="2"><path d="M12 21s-7-7-7-12a7 7 0 0 1 14 0c0 5-7 12-7 12z"/><circle cx="12" cy="9" r="2.5"/></svg></div>
    <div><h4 style="font-size:10px">Local Expertise</h4><p style="font-size:6.3px">Experienced sailors rooted in San Blas, honoring local culture with every voyage.</p></div>
  </div>
  <div class="feature" style="left:31px;top:1767px;width:220px;height:62px;padding:0 8px;gap:10px">
    <div class="fic" style="width:40px;height:40px"><svg width="18" height="18" viewBox="0 0 24 24" fill="none" stroke="#fff" stroke-width="2"><circle cx="12" cy="5" r="2"/><path d="M12 7v14M6 11h12M4 14a8 7 0 0 0 16 0"/></svg></div>
    <div><h4 style="font-size:10px">Handpicked Boats &amp; Captains</h4><p style="font-size:6.3px">We partner only with top-rated, trusted boats and captains for safety and quality.</p></div>
  </div>
  <div class="feature" style="left:31px;top:1837px;width:220px;height:62px;padding:0 8px;gap:10px">
    <div class="fic" style="width:40px;height:40px"><svg width="18" height="18" viewBox="0 0 24 24" fill="none" stroke="#fff" stroke-width="2"><circle cx="12" cy="12" r="8"/><path d="M12 6v12M8 10c2 0 4 1 4 4M16 10c-2 0-4 1-4 4"/></svg></div>
    <div><h4 style="font-size:10px">Sustainable Tourism</h4><p style="font-size:6.3px">Committed to eco-friendly travel that empowers Guna communities and preserves island beauty.</p></div>
  </div>
  <div class="feature" style="left:31px;top:1907px;width:220px;height:62px;padding:0 8px;gap:10px">
    <div class="fic" style="width:40px;height:40px"><svg width="18" height="18" viewBox="0 0 24 24" fill="none" stroke="#fff" stroke-width="2"><circle cx="12" cy="9" r="4"/><path d="M5 21a7 7 0 0 1 14 0M6 9a6 6 0 0 1 12 0"/></svg></div>
    <div><h4 style="font-size:10px">Fast &amp; Friendly Support</h4><p style="font-size:6.3px">From booking to boarding, our responsive team handles everything—stress-free and personalized.</p></div>
  </div>
  <div class="abs photo-sunset" role="img" aria-label="Sailboat at sea during a hazy sunset" style="left:281px;top:1719px;width:210px;height:230px;border-radius:22px 0 22px 0;border-top:2px solid var(--teal);border-right:2px solid var(--teal)"></div>

  <h2 class="abs sec-title" style="left:110px;top:2055px;width:300px;font-size:21px">Reviews</h2>
  <div class="review" style="left:47px;top:2127px;width:201px;height:100px">
    <div class="quote" style="left:30px;top:-14px;font-size:36px">“</div>
    <div class="rating" style="left:144px;top:14px"><b style="width:8px;height:8px"></b><span style="font-size:6px">★★★★★</span></div>
    <p class="abs" style="left:16px;top:34px;width:170px;font-size:5.6px">Sailing through the islands with this crew was the highlight of our year. Calm waters, fresh meals, warm people and beaches we will never forget. Every day felt easy and well planned from the first call.</p>
  </div>
  <div class="person" style="left:95px;top:2240px"><div class="avatar" style="width:26px;height:26px"></div><div><strong style="font-size:5.5px">MARTA DELGADO</strong><small style="font-size:5px">Guest, Spain</small></div></div>
  <div class="review" style="left:268px;top:2127px;width:202px;height:100px">
    <div class="quote" style="left:30px;top:-14px;font-size:36px">“</div>
    <div class="rating" style="left:145px;top:14px"><b style="width:8px;height:8px"></b><span style="font-size:6px">★★★★★</span></div>
    <p class="abs" style="left:16px;top:34px;width:170px;font-size:5.6px">Booking was quick and the captain knew every reef and island. Our kids snorkeled daily and loved it.</p>
  </div>
  <div class="person" style="left:314px;top:2240px"><div class="avatar" style="width:26px;height:26px"></div><div><strong style="font-size:5.5px">OWEN RAFFERTY</strong><small style="font-size:5px">Guest, Ireland</small></div></div>
  <div class="dots" style="left:243px;top:2290px"><span class="on"></span><span></span><span></span><span></span></div>

  <h2 class="abs sec-title" style="left:60px;top:2371px;width:400px;font-size:21px">Charter Inquiry Form</h2>
  <div class="abs form-bg" role="img" aria-label="Catamarans on turquoise water framing the form" style="left:0;top:2415px;width:520px;height:290px"></div>
  <form class="form-panel" style="left:92px;top:2435px;width:353px;height:240px">
    <div class="field" style="left:10px;top:27px;width:100px;height:19px;padding:0 8px;font-size:6.5px">Name</div>
    <div class="field" style="left:119px;top:27px;width:100px;height:19px;padding:0 8px;font-size:6.5px">Email</div>
    <div class="field" style="left:225px;top:27px;width:100px;height:19px;padding:0 8px;font-size:6.5px">Whatsapp Number</div>
    <div class="field" style="left:10px;top:55px;width:315px;height:19px;padding:0 8px;font-size:6.5px">Select Your Charter <span style="color:var(--orange)">⌄</span></div>
    <div class="field" style="left:10px;top:85px;width:100px;height:19px;padding:0 8px;font-size:6.5px">No.of Passengers <span style="color:var(--orange)">⇕</span></div>
    <div class="field" style="left:119px;top:85px;width:100px;height:19px;padding:0 8px;font-size:6.5px">Number of Days <span style="color:var(--orange)">⇕</span></div>
    <div class="field" style="left:225px;top:85px;width:100px;height:19px;padding:0 8px;font-size:6.5px">Date <span style="color:var(--sea-2)">▦</span></div>
    <div class="field" style="left:10px;top:111px;width:315px;height:19px;padding:0 8px;font-size:6.5px">What type of experience are you looking for? <span style="color:var(--orange)">⌄</span></div>
    <div class="field" style="left:10px;top:138px;width:315px;height:46px;padding:6px 8px;font-size:6.5px;align-items:flex-start">Message</div>
    <div class="abs btn btn-orange" style="left:134px;top:195px;width:58px;height:17px;font-size:7px">SUBMIT <span>↦</span></div>
  </form>

  <footer class="abs footer" style="left:0;top:2705px;width:520px;height:188px">
    <h5 class="foot-head" style="left:51px;top:44px;font-size:7.5px">QUICK LINKS</h5>
    <ul class="foot-list" style="left:55px;top:77px;font-size:5.8px;line-height:2.45"><li>Fleet</li><li>About Us</li><li>Contact</li><li>Pricing</li><li>Guna Yala</li></ul>
    <ul class="foot-list" style="left:111px;top:77px;font-size:5.8px;line-height:2.45"><li>Itineraries</li><li>Activities</li><li>Blog</li><li>Languages</li><li>BOOK NOW</li></ul>
    <h5 class="foot-head" style="left:200px;top:44px;font-size:7.5px">CONTACT US</h5>
    <div class="contact-row" style="left:200px;top:76px;font-size:5.5px"><i style="width:11px;height:11px;font-size:6px">✆</i><span>CALL US<br>0123 456 789</span></div>
    <div class="contact-row" style="left:200px;top:97px;font-size:5.5px"><i style="width:11px;height:11px;font-size:6px">✉</i><span>EMAIL US<br>hello@coralhopvoyages.net</span></div>
    <div class="contact-row" style="left:200px;top:118px;font-size:5.5px"><i style="width:11px;height:11px;font-size:6px">⌖</i><span>Address Line goes here,<br>Country Name, 4231</span></div>
    <h5 class="foot-head" style="left:342px;top:44px;font-size:7.5px">NEWSLETTER SIGN UP</h5>
    <div class="news-input" style="left:344px;top:80px;width:145px;height:20px;padding:0 9px;font-size:4.8px">ENTER YOUR EMAIL</div>
    <div class="news-btn" style="left:344px;top:109px;width:73px;height:16px;font-size:5.5px">SUBSCRIBE</div>
    <div class="abs" style="left:27px;top:159px;width:466px;height:1px;background:#2d5a69"></div>
    <p class="abs" style="left:27px;top:172px;font-size:5px;color:#e6eef2">Copyright © 2025 All Rights Reserved By Company name</p>
    <div class="socials" style="left:431px;top:168px"><span style="width:11px;height:11px"></span><span style="width:11px;height:11px"></span><span style="width:11px;height:11px"></span><span style="width:11px;height:11px"></span></div>
  </footer>
</section>

<!-- ================= MOBILE HOME (TOP) ================= -->
<section class="screen mobile-a">
  <header class="abs" style="left:0;top:0;width:184px;height:37px;background:#f3f9fc">
    <div class="abs logo" style="left:8px;top:11px;font-size:11px">Coral Hop Voyages</div>
    <svg class="abs" style="left:166px;top:15px" width="11" height="8" viewBox="0 0 11 8"><path d="M0 1h11M0 4h11M0 7h11" stroke="#f0912c" stroke-width="1"/></svg>
  </header>
  <div class="abs photo-sea" role="img" aria-label="Catamaran anchored on turquoise sea" style="left:0;top:37px;width:184px;height:140px"></div>
  <h1 class="abs hero-title" style="left:15px;top:70px;font-size:17px">San Blas Islands</h1>
  <p class="abs" style="left:15px;top:91px;width:90px;font-size:4px;color:#fff;line-height:1.3">Panama Sailing Vacations,Ultimate Beaches &amp; Catamaran Tours</p>
  <div class="abs btn btn-orange" style="left:15px;top:106px;width:62px;height:10px;font-size:3.6px">CHARTER INQUIRY FORM ↦</div>
  <div class="dots" style="left:86px;top:164px"><span class="on" style="width:2px;height:2px;background:#fff;border-color:#fff"></span><span style="width:2px;height:2px;border-color:#fff"></span><span style="width:2px;height:2px;border-color:#fff"></span></div>

  <h2 class="abs sec-title" style="left:12px;top:204px;width:160px;font-size:11px">Featured Sailing<br>Tour Packages</h2>
  <article class="abs card" style="left:26px;top:264px;width:132px;height:208px;border-radius:16px">
    <div class="abs card-photo photo-lagoon" role="img" aria-label="Aerial view of a white catamaran over clear water" style="left:5px;top:5px;width:122px;height:112px;border-radius:14px"></div>
    <div class="abs" style="left:12px;top:126px;width:115px">
      <div class="pkg-type" style="font-size:7px">Catamaran</div>
      <div class="pkg-name" style="font-size:11px">Aurora 42</div>
      <div class="pkg-meta" style="margin-top:3px;font-size:5.5px"><span><i></i>42 ft</span><span><i></i>3 cabin</span><span><i></i>8 Guest</span></div>
      <div class="pkg-note" style="margin-top:5px;font-size:5.3px">Service that exceeds all expectations!</div>
    </div>
    <div class="abs btn btn-blue" style="left:43px;top:200px;width:48px;height:10px;font-size:4.8px">INFO &amp; PRICE</div>
  </article>
  <div class="sq-arrow" style="left:78px;top:489px;width:14px;height:14px;background:#fff;box-shadow:0 1px 3px rgba(0,0,0,.18);color:var(--muted);font-size:7px">‹</div>
  <div class="sq-arrow" style="left:94px;top:489px;width:14px;height:14px;background:var(--orange);color:#fff;font-size:7px">›</div>
  <div class="abs btn btn-orange" style="left:26px;top:522px;width:132px;height:21px;font-size:7px">SEE ALL BOATS &amp; PRICES ↦</div>

  <h2 class="abs sec-title" style="left:8px;top:587px;width:168px;font-size:11px">Discover Ultimate<br>Panama Sailing Tours</h2>

  <article class="abs card" style="left:16px;top:649px;width:151px;height:239px;border-radius:12px">
    <div class="abs card-photo photo-party" role="img" aria-label="Couple walking along a marina dock" style="left:8px;top:10px;width:135px;height:106px"></div>
    <div class="icon-bubble" style="left:56px;top:-14px;width:38px;height:38px"><svg width="16" height="16" viewBox="0 0 24 24" fill="none" stroke="#fff" stroke-width="2"><circle cx="12" cy="5" r="2"/><path d="M12 7v14M6 11h12M4 14a8 7 0 0 0 16 0"/></svg></div>
    <h3 class="abs tour-title" style="left:0;top:128px;width:151px;font-size:11px">Private Charters</h3>
    <p class="abs tour-text" style="left:10px;top:146px;width:131px;font-size:6.2px">Sail the beautiful islands and beaches of San Blas on a private all-inclusive catamaran. Enjoy a custom itinerary, friendly crew, and flexible options to fit any budget—perfect for a relaxing escape.</p>
  </article>
  <article class="abs card" style="left:16px;top:918px;width:151px;height:237px;border-radius:12px">
    <div class="abs card-photo photo-party" role="img" aria-label="Group of friends celebrating on a sailboat deck" style="left:8px;top:10px;width:135px;height:106px"></div>
    <div class="icon-bubble" style="left:56px;top:-14px;width:38px;height:38px"><svg width="16" height="16" viewBox="0 0 24 24" fill="none" stroke="#fff" stroke-width="2"><circle cx="8" cy="6" r="2.5"/><circle cx="16" cy="6" r="2.5"/><path d="M4 21v-8a4 4 0 0 1 8 0v8M12 21v-8a4 4 0 0 1 8 0v8"/></svg></div>
    <h3 class="abs tour-title" style="left:0;top:128px;width:151px;font-size:11px">Shared Charters</h3>
    <p class="abs tour-text" style="left:10px;top:146px;width:131px;font-size:6.2px">Share the experience with others for a more affordable alternative to a private charter. Perfect for couples, solo travelers, and small groups—enjoy San Blas beaches, clear waters, great meals, and a relaxed atmosphere with a welcoming crew.</p>
  </article>
  <article class="abs card" style="left:16px;top:1186px;width:151px;height:238px;border-radius:12px">
    <div class="abs card-photo photo-bay" role="img" aria-label="Sailboat on calm turquoise water" style="left:8px;top:10px;width:135px;height:106px;border-radius:14px"></div>
    <div class="icon-bubble" style="left:56px;top:-14px;width:38px;height:38px"><svg width="16" height="16" viewBox="0 0 24 24" fill="none" stroke="#fff" stroke-width="2"><path d="M3 15h18l-3 5H6zM6 15V9h12v6M10 9V5h4v4"/></svg></div>
    <h3 class="abs tour-title" style="left:0;top:124px;width:151px;font-size:11px">Family Friendly<br>Boat Trips</h3>
    <p class="abs tour-text" style="left:10px;top:158px;width:131px;font-size:6.2px">San Blas is perfect for kids, with calm waters, safe snorkeling, and fun island-hopping. Families love the mix of adventure and culture—an ideal way to explore Panama together.</p>
  </article>

  <h2 class="abs sec-title" style="left:8px;top:1480px;width:168px;font-size:11px">Island Adventures &amp;<br>Activities</h2>
  <div class="abs card-photo photo-deck" role="img" aria-label="Friends cheering on the bow of a sailing yacht" style="left:7px;top:1547px;width:170px;height:169px;border-radius:8px"></div>
  <div class="abs" style="left:7px;top:1646px;width:170px;height:70px;border-radius:0 0 8px 8px;background:linear-gradient(180deg,rgba(15,95,134,0),rgba(15,95,134,.85))"></div>
  <div class="abs" style="left:7px;top:1664px;width:170px;text-align:center;font-family:var(--display);font-size:11px;color:#fff;font-weight:500">SAILING</div>
  <p class="abs" style="left:14px;top:1681px;width:156px;text-align:center;font-size:5.4px;color:#fff;line-height:1.5">Set sail across sparkling waters, hopping from one island group to another, each offering new beaches, and breathtaking views</p>
  <div class="arrow arrow-light" style="left:77px;top:1723px;width:11px;height:11px;font-size:6px">‹</div>
  <div class="arrow arrow-orange" style="left:94px;top:1723px;width:11px;height:11px;font-size:6px">›</div>
  <div class="dots" style="left:68px;top:1762px"><span class="on"></span><span></span><span></span><span></span><span></span><span></span><span></span></div>
</section>

<!-- ================= MOBILE HOME (BOTTOM) ================= -->
<section class="screen mobile-b">
  <h2 class="abs sec-title" style="left:12px;top:26px;width:160px;font-size:11px">Why Book With Us</h2>
  <div class="abs photo-sunset" role="img" aria-label="Sailboat at sea during a hazy sunset" style="left:18px;top:58px;width:144px;height:147px;border-radius:16px 0 16px 0;border-top:2px solid var(--teal);border-right:2px solid var(--teal)"></div>

  <div class="feature" style="left:18px;top:224px;width:147px;height:40px;padding:0 5px;gap:6px">
    <div class="fic" style="width:24px;height:24px"><svg width="12" height="12" viewBox="0 0 24 24" fill="none" stroke="#fff" stroke-width="2"><path d="M12 21s-7-7-7-12a7 7 0 0 1 14 0c0 5-7 12-7 12z"/><circle cx="12" cy="9" r="2.5"/></svg></div>
    <div><h4 style="font-size:6.5px">Local Expertise</h4><p style="font-size:4.2px">Experienced sailors rooted in San Blas, honoring local culture with every voyage.</p></div>
  </div>
  <div class="feature" style="left:18px;top:271px;width:147px;height:40px;padding:0 5px;gap:6px">
    <div class="fic" style="width:24px;height:24px"><svg width="12" height="12" viewBox="0 0 24 24" fill="none" stroke="#fff" stroke-width="2"><circle cx="12" cy="5" r="2"/><path d="M12 7v14M6 11h12M4 14a8 7 0 0 0 16 0"/></svg></div>
    <div><h4 style="font-size:6.5px">Handpicked Boats &amp; Captains</h4><p style="font-size:4.2px">We partner only with top-rated, trusted boats and captains for safety and quality.</p></div>
  </div>
  <div class="feature" style="left:18px;top:318px;width:147px;height:40px;padding:0 5px;gap:6px">
    <div class="fic" style="width:24px;height:24px"><svg width="12" height="12" viewBox="0 0 24 24" fill="none" stroke="#fff" stroke-width="2"><circle cx="12" cy="12" r="8"/><path d="M12 6v12"/></svg></div>
    <div><h4 style="font-size:6.5px">Sustainable Tourism</h4><p style="font-size:4.2px">Committed to eco-friendly travel that empowers Guna communities and preserves island beauty.</p></div>
  </div>
  <div class="feature" style="left:18px;top:365px;width:147px;height:40px;padding:0 5px;gap:6px">
    <div class="fic" style="width:24px;height:24px"><svg width="12" height="12" viewBox="0 0 24 24" fill="none" stroke="#fff" stroke-width="2"><circle cx="12" cy="9" r="4"/><path d="M5 21a7 7 0 0 1 14 0"/></svg></div>
    <div><h4 style="font-size:6.5px">Fast &amp; Friendly Support</h4><p style="font-size:4.2px">From booking to boarding, our responsive team handles everything—stress-free and personal.</p></div>
  </div>

  <h2 class="abs sec-title" style="left:12px;top:454px;width:160px;font-size:11px">Reviews</h2>
  <div class="review" style="left:14px;top:491px;width:158px;height:79px">
    <div class="quote" style="left:20px;top:-9px;font-size:28px">“</div>
    <div class="rating" style="left:114px;top:10px"><b style="width:6px;height:6px"></b><span style="font-size:5px">★★★★★</span></div>
    <p class="abs" style="left:12px;top:26px;width:136px;font-size:4.3px">Sailing through the islands with this crew was the highlight of our year. Calm waters, fresh meals and warm people. Every day felt easy and well planned from the very first call.</p>
  </div>
  <div class="person" style="left:52px;top:579px"><div class="avatar" style="width:20px;height:20px"></div><div><strong style="font-size:4.5px">MARTA DELGADO</strong><small style="font-size:4px">Guest, Spain</small></div></div>
  <div class="dots" style="left:79px;top:619px"><span class="on"></span><span></span><span></span></div>

  <h2 class="abs sec-title" style="left:8px;top:659px;width:168px;font-size:11px">Charter Inquiry Form</h2>
  <div class="abs form-bg" role="img" aria-label="Catamarans on turquoise water framing the form" style="left:0;top:697px;width:184px;height:146px"></div>
  <form class="form-panel" style="left:26px;top:707px;width:131px;height:128px;border-radius:8px">
    <div class="field" style="left:4px;top:6px;width:123px;height:10px;padding:0 4px;font-size:4px">Name</div>
    <div class="field" style="left:4px;top:21px;width:123px;height:10px;padding:0 4px;font-size:4px">Email</div>
    <div class="field" style="left:4px;top:36px;width:123px;height:10px;padding:0 4px;font-size:4px">Whatsapp Number</div>
    <div class="field" style="left:4px;top:51px;width:123px;height:10px;padding:0 4px;font-size:4px">Select Your Charter <span style="color:var(--orange)">⌄</span></div>
    <div class="field" style="left:4px;top:66px;width:42px;height:12px;padding:0 3px;font-size:3.6px">No.of Passengers</div>
    <div class="field" style="left:50px;top:66px;width:40px;height:12px;padding:0 3px;font-size:3.6px">No.of Days</div>
    <div class="field" style="left:94px;top:66px;width:33px;height:12px;padding:0 3px;font-size:3.6px">Date</div>
    <div class="field" style="left:4px;top:82px;width:123px;height:10px;padding:0 4px;font-size:4px">What type of experience are you looking for?</div>
    <div class="field" style="left:4px;top:96px;width:123px;height:16px;padding:2px 4px;font-size:4px;align-items:flex-start">Message</div>
    <div class="abs btn btn-orange" style="left:49px;top:116px;width:32px;height:8px;font-size:3.6px">SUBMIT ↦</div>
  </form>

  <footer class="abs footer" style="left:0;top:843px;width:184px;height:401px">
    <h5 class="foot-head" style="left:17px;top:19px;font-size:7.5px">QUICK LINKS</h5>
    <ul class="foot-list" style="left:17px;top:46px;font-size:5.6px;line-height:2.5"><li>Fleet</li><li>About Us</li><li>Contact</li><li>Pricing</li><li>Guna Yala</li></ul>
    <ul class="foot-list" style="left:74px;top:46px;font-size:5.6px;line-height:2.5"><li>Itineraries</li><li>Activities</li><li>Blog</li><li>Languages</li><li>BOOK NOW</li></ul>
    <h5 class="foot-head" style="left:17px;top:145px;font-size:7.5px">CONTACT US</h5>
    <div class="contact-row" style="left:17px;top:172px;font-size:5.4px"><i style="width:10px;height:10px;font-size:6px">✆</i><span>CALL US<br>0123 456 789</span></div>
    <div class="contact-row" style="left:17px;top:193px;font-size:5.4px"><i style="width:10px;height:10px;font-size:6px">✉</i><span>EMAIL US<br>hello@coralhopvoyages.net</span></div>
    <div class="contact-row" style="left:17px;top:214px;font-size:5.4px"><i style="width:10px;height:10px;font-size:6px">⌖</i><span>Address Line goes here,<br>Country Name, 4231</span></div>
    <h5 class="foot-head" style="left:17px;top:258px;font-size:7.5px">NEWSLETTER SIGN UP</h5>
    <div class="news-input" style="left:18px;top:288px;width:125px;height:16px;padding:0 8px;font-size:4.4px">ENTER YOUR EMAIL</div>
    <div class="news-btn" style="left:18px;top:313px;width:64px;height:14px;font-size:5px">SUBSCRIBE</div>
    <p class="abs" style="left:17px;top:353px;font-size:5.4px;color:#e6eef2;line-height:1.3">Copyright © 2025<br>All Rights Reserved By Company name</p>
    <div class="socials" style="left:17px;top:377px"><span style="width:13px;height:13px"></span><span style="width:13px;height:13px"></span><span style="width:13px;height:13px"></span><span style="width:13px;height:13px"></span></div>
  </footer>
</section>

</body>
</html>
```